Stationery Design Project for a consulting/educational company

We need a stationery design for a consulting / educational company called "VORN d.o.o.". We are an official partner (yet stand-alone company) of the TALMO Institute, Germany (www.talmo-example.de) that covers practically all themes regarding production optimisation, efectiveness, productivity (time studies, workplace organisation,...) We need the design for:

- a CERTIFICATE for seminar participates
- business cards
- letterhead

We are changing our webpage to their design, so we need to change the stationaries as well. I included 2 current logos, one with current color scheme (not important) and the other black/white with a frame. I also included the TALMO original certificate. Only the font + name"VORN" is important, the rest is up to you
Updates

Designs look good, but perhaps a gray & green combo would look nicer? Like on www.talmo-example.de? And without the frames?

Target Market(s)

Larger production companies top and middle management

Industry/Entity Type

Business

Requirements
Must have
• - the stationaries (all of them) should, besides the company name "VORN", also include the logo TALMO (in its color), like on their webpage www.talmo-example.de
Nice to have
• - certificate could use 5th color (e.g. silver) to make an impression
- similar color scheme to www.talmo-example.de

```html
<!DOCTYPE html>
<html lang="en">
<head>
<meta charset="utf-8">
<title>VORN – Certificate of Completion</title>
<link rel="stylesheet" href="https://fonts.googleapis.com/css2?family=Jost:ital,wght@0,400;0,600;1,700&family=Kaushan+Script&family=Source+Sans+3:wght@400&display=swap">
<style>
  :root {
    --backdrop: #1c1c1c;
    --paper: #ffffff;
    --ink: #111111;
    --grey: #5f5f61;
    --grey-swoosh: #6d6e71;
    --teal: #0aa6ad;
    --silver-light: #e6e7e8;
    --silver-dark: #9a9ca0;
    --dots: #ececec;
  }
  * { box-sizing: border-box; margin: 0; padding: 0; }
  html, body {
    width: 908px; height: 1200px; overflow: hidden;
    background: var(--backdrop);
  }
  .certificate {
    position: absolute; left: 66px; top: 59px;
    width: 768px; height: 1075px;
    background: var(--paper);
    border: 4px solid var(--silver-light);
    overflow: hidden;
    font-family: "Source Sans 3", sans-serif;
    color: var(--ink);
  }
  .certificate::after {
    content: ""; position: absolute; inset: 6px;
    border: 2px solid var(--silver-dark);
    pointer-events: none;
  }
  .dot-texture {
    position: absolute; left: 0; top: 250px; width: 768px; height: 800px;
    background: radial-gradient(ellipse 70% 45% at 75% 30%, var(--dots) 0%, rgba(236,236,236,0.6) 45%, rgba(255,255,255,0) 75%);
  }
  .decor-curves { position: absolute; left: 0; top: 0; width: 768px; height: 1075px; }
  .brand {
    position: absolute; top: 54px; left: 74px;
    font-family: "Jost", sans-serif; font-weight: 600;
    font-size: 132px; line-height: 1; letter-spacing: 4px;
    color: var(--ink);
  }
  .partner {
    position: absolute; top: 108px; left: 512px;
    display: flex; align-items: center; gap: 10px;
    font-family: "Jost", sans-serif; font-weight: 600;
    font-size: 40px; line-height: 1; color: var(--teal);
  }
  .partner .mark { width: 18px; height: 18px; background: var(--teal); }
  .centered { position: absolute; left: 0; width: 100%; text-align: center; line-height: 1; }
  .title {
    top: 258px; font-family: "Kaushan Script", cursive;
    font-size: 50px; color: var(--grey); letter-spacing: 1px;
  }
  .awarded {
    top: 424px; font-family: "Jost", sans-serif; font-style: italic; font-weight: 700;
    font-size: 29px; color: var(--grey);
  }
  .trainee {
    top: 475px; font-family: "Jost", sans-serif; font-weight: 400;
    font-size: 48px; color: var(--teal);
  }
  .reason { top: 655px; font-size: 26px; }
  .course { top: 703px; font-size: 40px; }
  .field {
    position: absolute; display: flex; align-items: baseline; gap: 30px;
    font-size: 22px; line-height: 1;
  }
  .field .line { display: block; border-bottom: 2px dotted var(--ink); height: 2px; }
  .field-date { left: 176px; top: 831px; }
  .field-date .line { width: 207px; }
  .field-signature { left: 221px; top: 892px; gap: 10px; }
  .field-signature .line { width: 209px; }
</style>
</head>
<body>
  <main class="certificate">
    <div class="dot-texture" role="img" aria-label="Soft grey halftone dot pattern in the background"></div>

    <svg class="decor-curves" viewBox="0 0 768 1075" aria-hidden="true">
      <path d="M0,863 Q384,1230 768,849 L768,1075 L0,1075 Z" fill="var(--teal)"/>
      <path d="M0,610 C40,850 250,1010 490,1025 C280,1015 80,920 0,760 Z" fill="var(--paper)"/>
      <path d="M0,627 C40,850 250,1000 472,1017 C280,1000 90,900 0,740 Z" fill="var(--grey-swoosh)"/>
    </svg>

    <div class="brand">VORN</div>
    <div class="partner"><span>TALMO</span><span class="mark"></span></div>

    <h1 class="centered title">Certificate of Completion</h1>
    <p class="centered awarded">Is Awarded To</p>
    <p class="centered trainee">Trainee Name</p>
    <p class="centered reason">for exellence in meeting all requirements of</p>
    <p class="centered course">Training course name</p>

    <div class="field field-date"><span>Completion Date</span><span class="line"></span></div>
    <div class="field field-signature"><span>Signature</span><span class="line"></span></div>
  </main>
</body>
</html>
```